Tallow Creek Stampede Sponsor Brochure/letter

We are wanting a professional looking brochure/letter that can be given to potential sponsors. This can be multiple pages the last page needs to be the Invoice (attached example) the prices on the example can be used.. this is a first nation rodeo and we are looking for sponsorship I can provide more photos if needed

Target Market(s)

This will be local corporate business's so this needs to be very professional looking

Industry/Entity Type

This is an event but we are looking for cooperate sponsorship

Font styles to use
Serif

Colors
0054AA
0677BA
7BADD7
CADEEF
E8F1F8
FFC000
F8CF3A
FAE287
FDF2CF
FEFAEE
F0912C
F2A743
F7CA91
FBE8D2
FDF5EE
EB3D1F
EC4F4E
F09395
F8D3D4
FCEDEE

Requirements
Must have
• The basic information, must have some quotes and photos can be multiple pages
Nice to have
• I would like to see that it is interactive, but gets to the point
Should not have
• no cartoon or must not look cheap

```html
<!DOCTYPE html>
<html lang="en">
<head>
<meta charset="utf-8">
<title>Tallow Creek Stampede – Sponsorship Proposal</title>
<link rel="stylesheet" href="https://fonts.googleapis.com/css2?family=Poppins:wght@400;500;600;700;800&family=Rubik+Mono+One&display=swap">
<style>
:root{
  --navy:#1b4e7d;
  --navy-dark:#123c63;
  --sky:#2b6194;
  --orange:#f0a22c;
  --orange-deep:#e8901c;
  --green:#6aa84f;
  --pale-blue:#dbe8f3;
  --rule:#d9dee4;
  --ink:#1f2a36;
  --muted:#5a6675;
  --stage:#f2f2f3;
  --gold:#cdb25a;
  --silver:#a3a8ae;
  --bronze:#b5611f;
  --platinum:#c8ced6;
}
*{box-sizing:border-box;margin:0;padding:0}
html,body{width:710px;height:1200px;overflow:hidden;background:var(--stage)}
body{font-family:"Poppins",sans-serif;color:var(--ink);position:relative}
.page{position:absolute;background:#fff;box-shadow:0 2px 6px rgba(0,0,0,.18);overflow:hidden}
.ph{position:absolute}
.url{position:absolute;left:0;right:0;text-align:center;font-size:6.5px;letter-spacing:3.2px;font-weight:600;color:var(--navy)}
.display{font-family:"Rubik Mono One",sans-serif}

/* cover */
.cover{left:195px;top:60px;width:320px;height:415px;background:var(--sky)}
.cover-photo{inset:0;background:linear-gradient(180deg,#2c5f8e 0%,#2a5a86 45%,#3b4f5e 72%,#5a4530 88%,#3d2a1a 100%)}
.rider{left:130px;top:38px;width:190px;height:330px;border-radius:40% 30% 20% 30%;background:radial-gradient(ellipse at 60% 55%,rgba(120,70,40,.85),rgba(120,70,40,0) 70%)}
.cover-title{position:absolute;left:16px;top:27px;width:212px}
.cover-title .rodeo{font-size:40px;line-height:1;color:var(--orange);letter-spacing:-1px}
.cover-title .sponsor{font-size:17.5px;line-height:1.05;color:#fff;margin-top:2px;letter-spacing:-.5px}
.cover-title .proposal{margin-top:6px;border-top:1px solid var(--orange);border-bottom:1px solid var(--orange);padding:4px 0;color:#fff;font-weight:500;font-size:15px;letter-spacing:17.5px}
.cover-band{position:absolute;left:0;top:168px;width:138px;height:76px;background:#fff;display:flex;align-items:center;justify-content:center;gap:6px}
.mark-dot{width:14px;height:14px;border-radius:50%;background:var(--green);flex:none}
.cover-band .name{font-size:9.5px;font-weight:600;color:var(--navy);line-height:1.15}
.cover .url{top:392px;color:var(--orange);font-size:8px;letter-spacing:4px}

/* letter page */
.letter{left:110px;top:503px;width:238px;height:307px}
.quote-mark{position:absolute;font-family:Georgia,serif;font-size:46px;line-height:1;color:var(--green);font-weight:700}
.quote{position:absolute;left:35px;top:19px;font-size:6px;font-weight:500;white-space:nowrap}
.quote-by{position:absolute;right:36px;top:27px;font-size:4px;font-weight:800;font-style:italic;color:var(--orange)}
.body-copy{position:absolute;left:13px;top:43px;width:213px;font-size:3.1px;line-height:1.35;color:var(--ink)}
.body-copy p{margin-bottom:3px}
.body-copy .lead{font-size:4px}
.contact-row{position:absolute;left:12px;top:124px;width:214px}
.brand-tag{position:absolute;left:0;top:0;font-size:4px;font-weight:700;color:var(--navy);line-height:1.1}
.brand-tag small{display:block;font-size:2.6px;color:var(--ink)}
.contact-hint{position:absolute;left:67px;top:0;font-size:3.3px;white-space:nowrap}
.contact-hint b{color:var(--navy)}
.pill{position:absolute;top:7px;height:7px;background:var(--green);color:#fff;font-size:4px;font-weight:600;display:flex;align-items:center;padding-left:3px;gap:4px;white-space:nowrap}
.pill .ico{width:8px;height:5px;background:var(--orange);display:flex;align-items:center;justify-content:center}
.ornament{left:95px;width:48px;height:18px;border-radius:9px;background:linear-gradient(90deg,#3b5a8c,#c8344a,#e2a63a,#c8344a,#3b5a8c)}
.letter-photo{left:12px;top:170px;width:214px;height:110px;border:2px solid var(--orange);background:linear-gradient(135deg,#c9ccc7,#8a9aa6 40%,#5b4634 75%,#b6b3a9)}
.letter .url{top:292px}

/* dates page */
.dates{left:362px;top:503px;width:238px;height:307px}
.section-title{position:absolute;font-size:6.8px;color:var(--navy);font-family:"Rubik Mono One",sans-serif;white-space:nowrap}
.tag{position:absolute;background:var(--orange);color:var(--ink);font-weight:700;font-size:5px;padding:0 3px;line-height:7px;white-space:nowrap}
.horses{left:130px;top:5px;width:95px;height:30px;border-radius:4px;background:linear-gradient(90deg,rgba(27,78,125,.12),rgba(27,78,125,.45))}
.date-item{position:absolute;top:43px;display:flex;gap:3px}
.date-box{width:23px;height:25px;background:var(--green);color:#fff;text-align:center;font-weight:700;line-height:1;flex:none}
.date-box .m{font-size:5px;padding-top:2px}
.date-box .d{font-size:12px}
.date-text{font-size:3.2px;font-weight:600;line-height:1.3;padding-top:3px;white-space:nowrap}
.free{position:absolute;left:12px;top:77px;font-size:11px;font-weight:800;color:var(--orange);line-height:1}
.free-text{position:absolute;left:44px;top:78px;font-size:3.6px;line-height:1.3;white-space:nowrap}
.free-text b{color:var(--navy);font-size:4.2px}
.culture{position:absolute;left:118px;top:79px;width:108px;height:9px;background:var(--orange);font-size:3.8px;font-weight:600;display:flex;align-items:center;justify-content:center;white-space:nowrap;clip-path:polygon(0 0,97% 0,100% 100%,3% 100%)}
.dates-copy{position:absolute;left:12px;top:97px;width:214px;font-size:3.1px;line-height:1.35}
.dates .ornament{top:114px}
.band-banner{position:absolute;left:86px;top:145px;width:140px;height:22px;background:var(--navy);color:#fff;font-weight:700;font-size:8px;white-space:nowrap;display:flex;align-items:center;justify-content:center;padding-left:6px;clip-path:polygon(5% 0,100% 0,100% 100%,0 100%)}
.band-photo{left:12px;top:168px;width:214px;height:110px;border:2px solid var(--navy);background:linear-gradient(180deg,#1b1b1b,#3a3a3a 40%,#6d8aa6 70%,#2a2a2a)}
.dates .url{top:292px}

/* packages page */
.packages{left:110px;top:822px;width:238px;height:307px}
.value-band{position:absolute;left:12px;top:12px;width:214px;height:15px;display:flex}
.value-band .l{background:var(--sky);color:#fff;font-size:6px;font-weight:600;display:flex;align-items:center;padding-left:4px;width:106px;white-space:nowrap}
.value-band .r{flex:1;background:var(--navy-dark);color:#fff;font-size:2.9px;font-weight:600;display:flex;align-items:center;padding-left:5px;line-height:1.2;white-space:nowrap;clip-path:polygon(0 0,100% 0,97% 100%,0 100%)}
.starter{position:absolute;left:12px;top:30px;width:214px;font-size:3.6px;color:var(--navy);font-weight:500;border-top:.5px solid var(--rule)}
.starter span{position:absolute;white-space:nowrap}
.pkg-grid{position:absolute;left:12px;width:214px;display:grid;grid-template-columns:repeat(4,1fr);gap:4px}
.pkg{background:var(--pale-blue);position:relative;height:105px}
.pkg.tall{height:116px}
.pkg-head{height:15px;color:#fff;text-align:center;line-height:1;padding-top:3px}
.pkg-head .t{font-size:6px;font-weight:700}
.pkg-head .s{font-size:2.6px;letter-spacing:1.5px;font-weight:500}
.pkg-head.two{padding-top:1px}
.pkg-head.two .t{font-size:5.4px;line-height:.95}
.gold .pkg-head{background:var(--gold)}
.silver .pkg-head{background:var(--silver)}
.bronze .pkg-head{background:var(--bronze)}
.platinum .pkg-head{background:var(--platinum);color:var(--ink)}
.orange .pkg-head{background:var(--orange)}
.green .pkg-head{background:var(--green)}
.pkg-sub{margin:2px auto 0;width:36px;background:#fff;text-align:center;font-size:3px;font-weight:700;color:var(--navy);line-height:1.1;padding:1px}
.pkg ul{list-style:none;padding:3px 3px 0 3px}
.pkg li{font-size:2.7px;line-height:1.15;padding-left:7px;position:relative;margin-bottom:2.6px}
.pkg li::before{content:"";position:absolute;left:1px;top:.5px;width:3px;height:2px;border-radius:1px 1px 0 0;background:var(--navy)}
.coin{left:6px;bottom:6px;width:38px;height:14px;border-radius:7px}
.gold .coin{background:linear-gradient(90deg,#b48a1c,#f2d06a,#b48a1c)}
.silver .coin{background:linear-gradient(90deg,#8e9399,#e6e8ea,#8e9399)}
.bronze .coin{background:linear-gradient(90deg,#b05a18,#f0a45c,#b05a18)}
.pkg-photo{left:4px;bottom:4px;width:42px;height:28px;border:.5px solid #bbb}
.pancake-photo{background:linear-gradient(160deg,#f4f1ec,#e9c9a2 55%,#b5374a)}
.kids-photo{background:linear-gradient(160deg,#fdfbf2,#f2d26b 50%,#6f9bd1)}
.packages .url{top:292px}

/* invoice page */
.invoice{left:362px;top:822px;width:238px;height:307px}
.inv-brand{position:absolute;left:13px;top:14px;display:flex;align-items:center;gap:4px}
.inv-brand .name{font-size:6px;font-weight:600;color:var(--navy);line-height:1.15}
.inv-title{position:absolute;left:93px;top:9px;font-size:12px;font-weight:800;color:var(--navy)}
.inv-contact{position:absolute;left:93px;top:26px;font-size:3.4px;line-height:1.9;white-space:nowrap}
.inv-contact i{display:inline-block;width:3px;height:3px;border-radius:50%;background:var(--orange);margin-right:3px;vertical-align:middle}
.inv-rule{position:absolute;left:93px;top:43px;width:145px;border-top:.5px solid var(--navy)}
.inv-form{position:absolute;left:12px;top:50px;width:214px;border:1px solid var(--navy);border-collapse:collapse}
.inv-form td{height:10px;font-size:3.6px}
.inv-form td.k{background:var(--navy);color:#fff;font-weight:600;width:57px;padding-left:6px}
.inv-form tr:nth-child(even) td.v{background:var(--pale-blue)}
.inv-table{position:absolute;left:12px;width:214px;border-collapse:collapse}
.inv-table th{background:var(--navy);color:#fff;font-weight:500;font-size:5.5px;height:16px;text-align:left;padding-left:6px}
.inv-table td{font-size:4.2px;height:11.4px;border-bottom:.5px solid var(--rule);font-weight:500;padding-left:1px;white-space:nowrap}
.inv-table td+td{border-left:.5px solid var(--rule)}
.inv-table td.c{padding-left:13px}
.inv-foot{position:absolute;left:12px;top:262px;width:214px;height:14px;border-bottom:.5px solid var(--rule);font-size:4.2px}
.inv-foot .paid{position:absolute;left:1px;top:1px;font-weight:500;line-height:1}
.inv-foot .paid small{display:block;font-size:2.8px;font-weight:400}
.inv-foot .chq{position:absolute;left:42px;top:2px;background:var(--orange);font-size:2.7px;font-weight:600;padding:0 3px;line-height:5px;white-space:nowrap;clip-path:polygon(0 0,95% 0,100% 100%,0 100%)}
.inv-foot .tot{position:absolute;left:149px;top:0;font-weight:500;line-height:1.05;border-left:.5px solid var(--rule);padding-left:7px;height:14px}
.inv-foot .tot::before{content:"";position:absolute;left:-52px;top:0;height:14px;border-left:.5px solid var(--rule)}
.invoice .url{top:292px}
</style>
</head>
<body>

<!-- Cover -->
<section class="page cover">
  <div class="ph cover-photo" role="img" aria-label="Sky and hills at dusk behind a bronc rider"></div>
  <div class="ph rider" role="img" aria-label="Cowboy riding a bucking paint horse"></div>
  <div class="cover-title">
    <div class="rodeo display">RODEO</div>
    <div class="sponsor display">SPONSORSHIP</div>
    <div class="proposal">PROPOSAL</div>
  </div>
  <div class="cover-band">
    <span class="mark-dot"></span>
    <span class="name">TALLOW CREEK<br>FIRST NATION</span>
  </div>
  <div class="url">www.tallowcreekfn.com</div>
</section>

<!-- Letter -->
<section class="page letter">
  <span class="quote-mark" style="left:10px;top:8px">“</span>
  <span class="quote-mark" style="right:6px;top:24px">”</span>
  <div class="quote">Courage is being scared to death and saddling up anyway!</div>
  <div class="quote-by">– HANK DELMORE</div>
  <div class="body-copy">
    <p>2 One day Rodeos with amazing prizes and buckles each day with the average winning a TCFN Drum! The Tallow Creek Stampede is an attraction to many local cowboys and cowgirls from local communities, Fort St. John and across BC, AB and surrounding areas. We offer youth to adult events that are all crowd pleasers.</p>
    <p>Since the beginning this has been an annual event up until Covid-19 when we have had to take a break but we are so excited to build it bigger and better then before!</p>
    <p>We have some big plans for the future of the Tallow Creek Stampede including an expansion of the Rodeo grounds, new event buildings, new office/announcer booths as well as the purchase of new grandstands. This will be a big endeavor that we think will benefit both our community as well as the local community.</p>
    <p><span class="lead">Our rodeo</span> would not have flourished without the support and generosity we have received from your sponsorship over the years. Once again, we are hoping your company will give generously to our yearly event and help continue to make our rodeo a success. All support goes towards any supplies not covered by donation, the purchase of materials to upgrade the rodeo grounds, rodeo stock and event payout. We hope to attract even more rodeo events, larger entertainers, and more fans through the gates. Your sponsorship will be highly regarded for what we hope will be generations to come.</p>
  </div>
  <div class="contact-row">
    <div class="brand-tag">TALLOW CREEK<br>STAMPEDE!<small>Your sponsorship is greatly appreciated.</small></div>
    <div class="contact-hint">For further information please Call or Email <b>MARLA QUINLAN</b></div>
    <div class="pill" style="left:67px;width:60px"><span class="ico">
      <svg width="4" height="4" viewBox="0 0 10 10"><path d="M2 1l2 2-1 1.5a6 6 0 0 0 2.5 2.5L7 6l2 2-1.5 1.5C4 9 1 6 .5 2.5z" fill="#fff"/></svg></span>250-555-0148</div>
    <div class="pill" style="left:132px;width:82px;font-size:3.4px"><span class="ico">
      <svg width="5" height="4" viewBox="0 0 10 8"><rect x=".5" y=".5" width="9" height="7" fill="none" stroke="#fff"/><path d="M.5 .5L5 4.5 9.5.5" fill="none" stroke="#fff"/></svg></span>mquinlan@tallowcreekfn.com</div>
  </div>
  <div class="ph ornament" style="top:147px" role="img" aria-label="Beaded floral ornament"></div>
  <div class="ph letter-photo" role="img" aria-label="Saddle bronc rider leaving the chute with cowboys watching"></div>
  <div class="url">www.tallowcreekfn.com</div>
</section>

<!-- Dates -->
<section class="page dates">
  <div class="section-title" style="left:12px;top:13px">RODEO DATES</div>
  <div style="position:absolute;left:12px;top:21px;font-size:2.8px;font-weight:600">July 28, 29, 30 2023</div>
  <div class="tag" style="left:12px;top:26px">EVENTS</div>
  <div class="ph horses" role="img" aria-label="Faint horse racing silhouettes"></div>
  <div class="date-item" style="left:12px"><div class="date-box"><div class="m">JULY</div><div class="d">28</div></div><div class="date-text">Gymkhana<br>and family<br>Dance</div></div>
  <div class="date-item" style="left:76px"><div class="date-box"><div class="m">JULY</div><div class="d">28</div></div><div class="date-text">Junior Rodeo at 11 am,<br>Main Rodeo starts at 2pm<br>with Steak Dinner and<br>Rodeo dance to follow<br>Band is Cedar Ridge Singers</div></div>
  <div class="date-item" style="left:164px"><div class="date-box"><div class="m">JULY</div><div class="d">28</div></div><div class="date-text">Junior Rodeo at<br>11 am, Main Rodeo<br>starts at 2pm</div></div>
  <div class="free">FREE</div>
  <div class="free-text"><b>PANCAKE BREAKFAST BOTH</b><br>both Saturday and Sunday Morning</div>
  <div class="culture">Cultural Events happening throughout the day</div>
  <div class="dates-copy">Saddle up for the Tallow Creek Stampede held at the Tallow Creek First Nation Rodeo grounds! This is now a 3 day family fun event with the addition of a Friday afternoon Gymkhana! Tallow Creek Stampede has been running for over 30 years and we are exciting to bring the excitement back.</div>
  <div class="ph ornament" role="img" aria-label="Beaded floral ornament"></div>
  <div class="section-title" style="left:12px;top:145px">INFORMATION</div>
  <div class="tag" style="left:12px;top:155px;font-size:5.6px;line-height:8px">DANCE – JULY 29</div>
  <div class="band-banner">THE CEDAR RIDGE SINGERS</div>
  <div class="ph band-photo" role="img" aria-label="Drummers in cowboy hats singing with hand drums"></div>
  <div class="url">www.tallowcreekfn.com</div>
</section>

<!-- Packages -->
<section class="page packages">
  <div class="value-band"><div class="l">SHARE YOU COMPANIES VALUE</div><div class="r">HAVE A LOOK AND LET US KNOW HOW WE CAN HELP<br>YOU CONNECT WITH THE RIGHT NETWORK FOR YOU.</div></div>
  <div class="starter">
    <span style="left:9px;top:4px">Rodeo Packages</span>
    <span style="left:9px;top:12px">Starter package</span>
    <span style="left:55px;top:4px">Company logo on the big screen</span>
    <span style="left:55px;top:12px">Company logo on Web and program</span>
    <span style="left:139px;top:4px">2 Admission tickets to Sunday rodeo</span>
  </div>
  <div class="pkg-grid" style="top:55px">
    <div class="pkg gold"><div class="pkg-head"><div class="t">GOLD</div><div class="s">PACKAGE</div></div>
      <ul><li>Social media Ads and mentions</li><li>Company logo on Big screen</li><li>Company logo on Web</li><li>4 admission tickets to Sunday Rodeo</li></ul>
      <div class="ph coin" role="img" aria-label="Gold coins"></div></div>
    <div class="pkg silver"><div class="pkg-head"><div class="t">SILVER</div><div class="s">PACKAGE</div></div>
      <ul><li>Social media Ads and mentions</li><li>Company logo on Big screen</li><li>Company logo on Web</li><li>Banner (sponsor provided) in arena</li><li>4 weekend passes</li></ul>
      <div class="ph coin" role="img" aria-label="Silver coins"></div></div>
    <div class="pkg bronze"><div class="pkg-head"><div class="t">BRONZE</div><div class="s">PACKAGE</div></div>
      <ul><li>Social media Ads and mentions</li><li>Company logo on Big screen</li><li>Company logo on Web</li><li>Banner (sponsor provided) in arena</li><li>6 weekend passes</li><li>6 Dance tickets (must be age of majority) including steak dinner</li></ul>
      <div class="ph coin" role="img" aria-label="Bronze coins"></div></div>
    <div class="pkg platinum"><div class="pkg-head"><div class="t">PLATINUM</div><div class="s">PACKAGE</div></div>
      <ul><li>Pre event Radio advertising</li><li>Company logo on posters</li><li>Social media Ads and mentions</li><li>Company logo on Big screen</li><li>Company logo on Web</li><li>Commercial on the big screen</li><li>2 large Banners (sponsor provided) in arena</li><li>8 weekend passes</li><li>8 Dance tickets (must be age of majority) including steak dinner</li></ul></div>
  </div>
  <div class="pkg-grid" style="top:166px">
    <div class="pkg tall orange"><div class="pkg-head"><div class="t">SALOON</div><div class="s">PACKAGE</div></div>
      <ul><li>Pre event Radio advertising</li><li>Company logo on posters</li><li>Social media Ads and mentions</li><li>Company logo on Big screen</li><li>Company logo on Web</li><li>Commercial on the big screen</li><li>2 large Banners (sponsor provided) in arena</li><li>6 weekend passes</li><li>8 Dance tickets (must be age of majority) including steak dinner</li></ul></div>
    <div class="pkg tall green"><div class="pkg-head two"><div class="t">PANCAKE<br>BREAKFAST</div><div class="s">PACKAGE</div></div>
      <div class="pkg-sub">2 MORNINGS</div>
      <ul><li>Social media Ads and mentions</li><li>Company logo on Big screen</li><li>Company logo on Web</li><li>4 weekend passes</li></ul>
      <div class="ph pkg-photo pancake-photo" role="img" aria-label="Stack of pancakes with berries"></div></div>
    <div class="pkg tall orange"><div class="pkg-head"><div class="t">KIDS FUN</div><div class="s">PACKAGE</div></div>
      <div class="pkg-sub">KIDS EVENTS DURING INTERMISSION</div>
      <ul><li>Company logo on the big screen</li><li>Company logo on Web and program</li><li>Social Media Ads and Mentions</li><li>2 weekend passes</li></ul>
      <div class="ph pkg-photo kids-photo" role="img" aria-label="Children at play in an early education setting"></div></div>
    <div class="pkg tall green"><div class="pkg-head two"><div class="t">STEAK<br>DINNER</div></div>
      <ul><li>Pre event Radio advertising</li><li>Company logo on posters</li><li>Social media Ads and mentions</li><li>Company logo on Big screen</li><li>Company logo on Web</li><li>Commercial on the big screen</li><li>2 large Banners (sponsor provided) in arena</li><li>6 weekend passes</li><li>6 Dance tickets (must be age of majority) including steak dinner</li></ul></div>
  </div>
  <div class="url">www.tallowcreekfn.com</div>
</section>

<!-- Invoice -->
<section class="page invoice">
  <div class="inv-brand"><span class="mark-dot" style="width:9px;height:9px"></span><span class="name">TALLOW CREEK<br>FIRST NATION</span></div>
  <div class="inv-title">INVOICE</div>
  <div class="inv-contact">
    <div><i></i>250-555-0148 &nbsp;|&nbsp; <i></i>office@tallowcreekfn.com</div>
    <div><i></i>Tallow Creek PO Box 12 Ridgeview BC V0C 1Z0</div>
  </div>
  <div class="inv-rule"></div>
  <table class="inv-form">
    <tr><td class="k">COMPANY NAME</td><td class="v"></td></tr>
    <tr><td class="k">ATTENTION</td><td class="v"></td></tr>
    <tr><td class="k">ADDRESS</td><td class="v"></td></tr>
    <tr><td class="k">PHONE NUMBER</td><td class="v"></td></tr>
    <tr><td class="k">DATE</td><td class="v"></td></tr>
  </table>
  <table class="inv-table" style="top:106px">
    <tr><th style="width:94px">Rodeo Packages</th><th style="width:42px">Quantity</th><th style="width:39px">Cost</th><th>Total</th></tr>
    <tr><td>Starter Packages</td><td></td><td class="c">$ 750</td><td></td></tr>
    <tr><td>Starter Packages</td><td></td><td class="c">$ 1500</td><td></td></tr>
    <tr><td>Starter Packages</td><td></td><td class="c">$ 3000</td><td></td></tr>
    <tr><td>Starter Packages</td><td></td><td class="c">$ 5000</td><td></td></tr>
    <tr><td>Starter Packages</td><td></td><td class="c">$ 7500</td><td></td></tr>
  </table>
  <table class="inv-table" style="top:185px">
    <tr><th colspan="4">Event Packages</th></tr>
    <tr><td style="width:94px">Fun Packages</td><td style="width:42px"></td><td class="c" style="width:39px">$ 1000</td><td></td></tr>
    <tr><td>Dance Salmon Packages</td><td></td><td class="c">$ 6000</td><td></td></tr>
    <tr><td>Steak Dinner Packages</td><td></td><td class="c">$ 4000</td><td></td></tr>
    <tr><td>Pancake Breakfast Packages</td><td></td><td class="c">$ 2000</td><td></td></tr>
    <tr><td>Starter Packages</td><td></td><td class="c">$ 2000</td><td></td></tr>
  </table>
  <div class="inv-foot">
    <div class="paid">Paid by Cheque<small>MEMO RODEO</small></div>
    <div class="chq">TALLOW CREEK FIRST NATION</div>
    <div class="tot">Total<br>Invoice</div>
  </div>
  <div class="url">www.tallowcreekfn.com</div>
</section>

</body>
</html>
```